Engineering Consultant Business Card

I'm starting a new business as a high-end engineering consultant in a niche field. I've attached the jpg for my logo plus the branding guideline document that I've been following. You can see my business website here: www.tarvikworks.com
I'd like a business card that has the logo on one side, then the other side has (in any order): Tarvik Works, Inc.
Dana Whitlock
President and Chief EMC Engineer
www.tarvikworks.com
dana@tarvikworks.com
Optional: motto "We will solve your EMC problems as early as possible—ideally before they even start."
I'm not planning on including a phone number
Target Market(s)
Businesses, especially makers of electronics hardware
Industry/Entity Type
Electrical engineering
Contact Information for Business Card
Company name, my name, website, email

```html
<!DOCTYPE html>
<html lang="en">
<head>
<meta charset="utf-8">
<title>Tarvik Works, Inc. — Business Card</title>
<link rel="stylesheet" href="https://fonts.googleapis.com/css2?family=Jost:wght@400;500;600&display=swap">
<style>
  :root {
    --page-bg: #e9e9eb;
    --card-white: #ffffff;
    --card-blue: #2b3f94;
    --card-blue-deep: #22358a;
    --brand-blue: #2e44a0;
    --accent-sky: #8fd0ee;
    --ink-white: #ffffff;
    --schematic-tone: #d9dadd;
  }
  * { box-sizing: border-box; margin: 0; padding: 0; }
  html, body {
    width: 1200px; height: 900px; overflow: hidden;
    background: var(--page-bg);
    font-family: "Jost", "Futura", sans-serif;
  }
  .sheet {
    width: 1200px; height: 900px;
    display: flex; flex-direction: column; align-items: center; justify-content: center;
    gap: 44px;
  }
  .card {
    position: relative;
    width: 600px; height: 343px;
    overflow: hidden;
    box-shadow: 0 8px 24px rgba(0,0,0,0.18);
  }
  /* Front side */
  .card--front {
    background: linear-gradient(160deg, #ffffff 0%, #f3f3f4 100%);
    border-radius: 44px 0 44px 0;
  }
  .schematic-area {
    position: absolute; left: 34px; top: 30px;
    width: 360px; height: 283px;
    background: linear-gradient(135deg, #e4e5e8, var(--schematic-tone));
    border-radius: 4px;
  }
  .brandmark {
    position: absolute; display: flex; align-items: center; gap: 12px;
    font-weight: 600; letter-spacing: 0.02em; white-space: nowrap;
  }
  .card--front .brandmark {
    right: 34px; top: 150px; color: var(--brand-blue); font-size: 30px;
  }
  .brandmark__dot {
    width: 26px; height: 26px; border-radius: 50%; background: currentColor; flex: none;
  }
  /* Back side */
  .card--back {
    background: linear-gradient(90deg, var(--card-blue-deep) 0%, var(--card-blue) 100%);
    border-radius: 0 44px 0 44px;
    color: var(--ink-white);
  }
  .card--back .brandmark {
    right: 34px; top: 118px; color: var(--ink-white); font-size: 30px;
  }
  .identity {
    position: absolute; left: 44px; top: 58px; width: 330px;
  }
  .identity__name {
    color: var(--accent-sky); font-weight: 600; font-size: 22px;
    letter-spacing: 0.04em; text-transform: uppercase; line-height: 1.1;
  }
  .identity__title {
    font-size: 17px; font-weight: 400; margin-top: 2px;
  }
  .contact { list-style: none; margin-top: 22px; }
  .contact__item {
    display: flex; align-items: center; gap: 10px;
    font-size: 17px; line-height: 1.45;
  }
  .contact__icon { width: 18px; height: 18px; flex: none; }
  .motto {
    margin-top: 28px; color: var(--accent-sky);
    font-size: 15px; line-height: 1.35;
  }
</style>
</head>
<body>
  <main class="sheet">
    <section class="card card--front" aria-label="Card front">
      <div class="schematic-area" role="img" aria-label="Power supply circuit schematic drawing"></div>
      <div class="brandmark"><span class="brandmark__dot"></span>Tarvik Works</div>
    </section>

    <section class="card card--back" aria-label="Card back">
      <div class="identity">
        <h1 class="identity__name">Dana Whitlock</h1>
        <p class="identity__title">President and Chief EMC Engineer</p>
        <ul class="contact">
          <li class="contact__item">
            <svg class="contact__icon" viewBox="0 0 18 18" aria-hidden="true">
              <rect x="1.5" y="4" width="15" height="10" fill="none" stroke="#fff" stroke-width="1.5"/>
              <path d="M1.5 4 L9 10 L16.5 4" fill="none" stroke="#fff" stroke-width="1.5"/>
            </svg>
            dana@tarvikworks.com
          </li>
          <li class="contact__item">
            <svg class="contact__icon" viewBox="0 0 18 18" aria-hidden="true">
              <circle cx="9" cy="9" r="7.5" fill="none" stroke="#fff" stroke-width="1.3"/>
              <ellipse cx="9" cy="9" rx="3.3" ry="7.5" fill="none" stroke="#fff" stroke-width="1.1"/>
              <path d="M1.5 9 H16.5 M3 5 H15 M3 13 H15" stroke="#fff" stroke-width="1.1"/>
            </svg>
            www.tarvikworks.com
          </li>
        </ul>
        <p class="motto">We will solve your EMC problems as early as possible—<br>Ideally before they even start.</p>
      </div>
      <div class="brandmark"><span class="brandmark__dot"></span>Tarvik Works</div>
    </section>
  </main>
</body>
</html>
```